Business Card for Holistic Health Business
Bright Ferns Natural Wellness & Live Cell Review
Use same font as used in my logo
Not sure, I am open to different fonts.
Simple
Marla Dunwoody
DynBC, CH, BA
Larkvale Acupuncture Clinic
2736-18 Avenue, Suite 200
Larkvale, AB T8K 2P6
brightferns@mailnest.ca
www.brightfernsnaturalwellness.com
Logo for Bright Ferns business card.

```html
<!DOCTYPE html>
<html lang="en">
<head>
<meta charset="utf-8">
<title>Bright Ferns Business Card</title>
<link href="https://fonts.googleapis.com/css2?family=Open+Sans:wght@400;600;700&display=swap" rel="stylesheet">
<style>
  :root {
    --page-bg: #e9e9e7;
    --band-dark: #1c2128;
    --band-mid: #4b5662;
    --card-white: #ffffff;
    --card-grey: #e4e6e8;
    --ink: #2b2f33;
    --ink-soft: #5d6368;
    --accent-blue: #3b82c4;
    --stripe-black: #111315;
  }
  * { margin: 0; padding: 0; box-sizing: border-box; }
  html, body { width: 1200px; height: 896px; overflow: hidden; }
  body {
    background: var(--page-bg);
    font-family: "Open Sans", Arial, sans-serif;
    color: var(--ink);
    position: relative;
  }
  .card {
    position: absolute;
    width: 560px;
    height: 300px;
    overflow: hidden;
    box-shadow: 0 6px 18px rgba(0,0,0,0.18);
  }
  .card--contact { left: 90px; top: 70px; background: linear-gradient(180deg, #fafafa, var(--card-grey)); }
  .card--brand { left: 550px; top: 500px; background: radial-gradient(ellipse at 50% 40%, var(--card-white) 0%, var(--card-grey) 100%); }

  .contact-band {
    position: absolute; left: 0; top: 0; width: 100%; height: 138px;
    background:
      repeating-linear-gradient(90deg, rgba(255,255,255,0.04) 0 6px, rgba(0,0,0,0.06) 6px 14px),
      linear-gradient(180deg, var(--band-mid) 0%, var(--band-dark) 100%);
  }
  .wordmark { position: absolute; display: flex; flex-direction: column; align-items: flex-start; }
  .wordmark__row { display: flex; align-items: center; gap: 8px; }
  .wordmark__dot { width: 12px; height: 12px; border-radius: 50%; background: var(--accent-blue); }
  .wordmark__name { font-size: 34px; font-weight: 600; color: var(--ink); line-height: 1; letter-spacing: 0.5px; }
  .wordmark__tagline { font-size: 11.5px; color: var(--ink); margin-top: 6px; padding-top: 3px; border-top: 1px solid var(--ink); }
  .card--contact .wordmark { left: 175px; top: 30px; }
  .card--contact .wordmark__name, .card--contact .wordmark__tagline { color: #111; }
  .card--contact .wordmark__tagline { border-color: #111; }
  .card--contact .contact-band + .wordmark .wordmark__name { color: #0e1114; }

  .person { position: absolute; left: 24px; top: 170px; }
  .person__name { font-size: 14px; font-weight: 700; color: var(--accent-blue); }
  .person__creds { font-size: 11px; color: var(--ink-soft); margin-top: 6px; }

  .contact-list { position: absolute; left: 320px; top: 168px; list-style: none; font-size: 11px; color: var(--ink-soft); line-height: 17px; }
  .contact-list li { display: flex; align-items: center; gap: 6px; }
  .contact-list li.no-icon { padding-left: 16px; }
  .contact-list svg { width: 10px; height: 10px; flex: none; }

  .card--brand .wordmark { left: 130px; top: 105px; }
  .brand-stripes { position: absolute; left: 0; bottom: 0; width: 100%; height: 26px; }
</style>
</head>
<body>
  <section class="card card--contact">
    <div class="contact-band"></div>
    <div class="wordmark">
      <div class="wordmark__row">
        <span class="wordmark__dot"></span>
        <span class="wordmark__name">Bright Ferns</span>
      </div>
      <span class="wordmark__tagline">Natural Wellness &amp; Live Cell Review</span>
    </div>
    <div class="person">
      <p class="person__name">Marla Dunwoody</p>
      <p class="person__creds">DynBC, CH, BA</p>
    </div>
    <ul class="contact-list">
      <li><svg viewBox="0 0 10 10"><circle cx="5" cy="5" r="5" fill="#3b82c4"/><path d="M5 2.2a1.8 1.8 0 0 1 1.8 1.8C6.8 5.4 5 7.8 5 7.8S3.2 5.4 3.2 4A1.8 1.8 0 0 1 5 2.2z" fill="#fff"/></svg>Larkvale Acupuncture Clinic</li>
      <li class="no-icon">2736-18 Avenue, Suite 200</li>
      <li class="no-icon">Larkvale, AB T8K 2P6</li>
      <li><svg viewBox="0 0 10 10"><circle cx="5" cy="5" r="5" fill="#3b82c4"/><path d="M3.3 2.6l1 1-.6.7a4 4 0 0 0 2 2l.7-.6 1 1-.7.8C5 7.3 2.7 5 2.5 3.3z" fill="#fff"/></svg>780.555.0148</li>
      <li><svg viewBox="0 0 10 10"><circle cx="5" cy="5" r="5" fill="#3b82c4"/><rect x="2.4" y="3.2" width="5.2" height="3.6" fill="#fff"/><path d="M2.4 3.2L5 5.3l2.6-2.1" stroke="#3b82c4" stroke-width=".6" fill="none"/></svg>brightferns@mailnest.ca</li>
      <li><svg viewBox="0 0 10 10"><circle cx="5" cy="5" r="5" fill="#3b82c4"/><circle cx="5" cy="5" r="2.6" stroke="#fff" stroke-width=".7" fill="none"/><path d="M2.4 5h5.2M5 2.4v5.2" stroke="#fff" stroke-width=".6"/></svg>www.brightfernsnaturalwellness.com</li>
    </ul>
  </section>

  <section class="card card--brand">
    <div class="wordmark">
      <div class="wordmark__row">
        <span class="wordmark__dot"></span>
        <span class="wordmark__name">Bright Ferns</span>
      </div>
      <span class="wordmark__tagline">Natural Wellness &amp; Live Cell Review</span>
    </div>
    <svg class="brand-stripes" viewBox="0 0 560 26" preserveAspectRatio="none">
      <polygon points="0,12 300,12 290,26 0,26" fill="#111315"/>
      <polygon points="330,10 560,0 560,26 318,26" fill="#3b82c4"/>
    </svg>
  </section>
</body>
</html>
```